Webdesign Chiropraktik
Zielgruppe
Amerikanische Chiropraktik
Aufgabenstellung
keine direkten vorgaben...Wir sind ein junges Team und brauchen eine moderne ansprechende Webseite...

```html
<!DOCTYPE html>
<html lang="de">
<head>
<meta charset="utf-8">
<title>PraxisVolden – Amerikanische Chiropraktik</title>
<link href="https://fonts.googleapis.com/css2?family=Bebas+Neue&family=Oswald:wght@600&family=Poppins:wght@400;500;600&display=swap" rel="stylesheet">
<style>
:root{
  --mint:#edfbe9;
  --green:#45b535;
  --ink:#2d2d2d;
  --muted:#8e9a8b;
  --grey:#9a9a9a;
  --photo-dark:#3e3a37;
  --photo-warm:#8a7465;
  --white:#ffffff;
}
*{margin:0;padding:0;box-sizing:border-box}
html,body{width:1200px;height:863px;overflow:hidden;background:var(--white);font-family:'Poppins',sans-serif;color:var(--ink)}
.hero{position:relative;height:611px;background:var(--mint)}
.hero-photo{position:absolute;left:675px;top:0;width:525px;height:611px;
  background:linear-gradient(160deg,#5a5652 0%,var(--photo-dark) 40%,var(--photo-warm) 75%,#b39a88 100%);
  border-bottom-left-radius:170px 230px}
.logo{position:absolute;left:100px;top:19px;font-family:'Oswald',sans-serif;font-weight:600;font-size:23px;color:var(--green);letter-spacing:-.3px}
.nav{position:absolute;left:373px;top:26px;display:flex;gap:27px;font-size:11.5px}
.nav a{color:var(--ink);text-decoration:none}
.social{position:absolute;display:flex}
.social span{display:block;border-radius:50%;background:var(--ink)}
.social-top{left:794px;top:16px;gap:17px}
.social-top span{width:25px;height:25px;background:#4a4a4a}
.social-hero{left:100px;top:532px;gap:30px}
.social-hero span{width:37px;height:37px}
.btn{position:absolute;display:flex;align-items:center;justify-content:center;background:var(--green);color:var(--white);border-radius:30px;font-size:11.5px;font-weight:500}
.btn-top{left:949px;top:19px;width:151px;height:30px}
.btn-hero{left:100px;top:423px;width:150px;height:38px;box-shadow:0 12px 24px rgba(69,181,53,.18)}
.headline{position:absolute;left:112px;top:138px;font-family:'Bebas Neue',sans-serif;font-weight:400;font-size:86px;line-height:80px;color:var(--ink)}
.lead{position:absolute;left:100px;top:324px;width:400px;font-size:16px;line-height:25px;color:var(--muted)}
.contact-link{position:absolute;left:280px;top:432px;font-size:12px;color:var(--ink);display:flex;align-items:center;gap:12px}
.contact-link u{text-underline-offset:2px}
.hotline{position:absolute;left:900px;top:485px;width:200px;height:62px;background:var(--white);border-radius:31px;display:flex;align-items:center;padding-left:11px;gap:11px}
.hotline-icon{width:36px;height:36px;border-radius:50%;background:#eef8ec;display:flex;align-items:center;justify-content:center}
.hotline-label{font-size:11px;color:var(--green);line-height:16px}
.hotline-number{font-size:15px;font-weight:600;color:var(--ink)}
.slider-arrows{position:absolute;left:1024px;top:580px;display:flex;gap:26px}
.intro{padding:72px 100px 0}
.intro h2{font-family:'Bebas Neue',sans-serif;font-weight:400;font-size:31px;line-height:32px;margin-left:4px}
.intro h3{font-weight:400;font-size:16px;color:var(--grey);margin:10px 0 0 4px}
.intro p{font-size:12.4px;line-height:25px;margin-top:6px;width:1002px}
</style>
</head>
<body>
<section class="hero">
  <div class="hero-photo" role="img" aria-label="Chiropraktiker behandelt den Nacken einer liegenden Patientin"></div>
  <div class="logo">PraxisVolden</div>
  <nav class="nav"><a href="#">Home</a><a href="#">Ablauf</a><a href="#">Team</a><a href="#">Kontakt</a></nav>
  <div class="social social-top"><span></span><span></span><span></span></div>
  <a class="btn btn-top">Termin verabreden</a>
  <h1 class="headline">Amerikanische<br>Chiropraktik.</h1>
  <p class="lead">Endlich gibt es auch amerikanische Chiropraktik in Erding</p>
  <a class="btn btn-hero">Termin verabreden</a>
  <div class="contact-link"><u>Contact Us</u>
    <svg width="15" height="8" viewBox="0 0 15 8"><path d="M0 4h13M10 1l3 3-3 3" stroke="#2d2d2d" stroke-width="1.5" fill="none"/></svg></div>
  <div class="social social-hero"><span></span><span></span><span></span></div>
  <div class="hotline">
    <div class="hotline-icon"><svg width="16" height="16" viewBox="0 0 24 24"><path d="M22 16.9v3a2 2 0 0 1-2.2 2 19.8 19.8 0 0 1-8.6-3.1 19.5 19.5 0 0 1-6-6A19.8 19.8 0 0 1 2.1 4.2 2 2 0 0 1 4.1 2h3a2 2 0 0 1 2 1.7c.1.9.4 1.8.7 2.7a2 2 0 0 1-.5 2.1L8 9.8a16 16 0 0 0 6 6l1.3-1.3a2 2 0 0 1 2.1-.4c.9.3 1.8.6 2.7.7a2 2 0 0 1 1.7 2z" stroke="#45b535" stroke-width="1.8" fill="none"/></svg></div>
    <div><div class="hotline-label">Hotline</div><div class="hotline-number">0800 5550147</div></div>
  </div>
  <div class="slider-arrows">
    <svg width="26" height="14" viewBox="0 0 26 14"><path d="M26 7H3M8 2 3 7l5 5" stroke="#c8c8c8" stroke-width="2.5" fill="none"/></svg>
    <svg width="26" height="14" viewBox="0 0 26 14"><path d="M0 7h23M18 2l5 5-5 5" stroke="#ffffff" stroke-width="2.5" fill="none"/></svg>
  </div>
</section>
<section class="intro">
  <h2>Chiropraktik in Erding</h2>
  <h3>Amerikanische Chiropraktik nun auch in Erding!</h3>
  <p>Die Chiropraktik beschäftigt sich primär mit den Störungen des Nervensystems im Körper. Gibt es in unserem Hauptorgan (Gehirn) einen Fehler/Schwäche kann sich das in unserem Körper spiegeln! Meistens reagiert der Körper mit einer lokalen Verspannung eines Muskels. Daraus kann eine Einschränkung der</p>
</section>
</body>
</html>
```